Sign for Pilates Studio

Cute and fun sandwich board sign ( 36" x 24" ) for outstanding Pilates studio in Santa Cruz. Sign should have logo, use the phrase "Pilates & Kinovane classes 7 Days a Week"
Updates

Dimensions are 36" x 24" and it should be clear and simple. The goal is to get people in the door. Try using the tree theme or the circle theme. Colors can be simple green, gold, burgundy....black lettering probably... Added Monday, January 12, 2015

Target Market(s)

Hip 30 year olds and everyone else too

Requirements
Must have
• It's a freestanding sign and should be simple to read
• Must say "Lark Hollow Pilates"
• "Pilates Classes 7 days A week"
Nice to have
• Logo, tree. green and gold colors
Should not have
• Not too busy. Easy to read while driving by

```html
<!DOCTYPE html>
<html lang="en">
<head>
<meta charset="utf-8">
<title>Lark Hollow Pilates – Sandwich Board</title>
<link rel="stylesheet" href="https://fonts.googleapis.com/css2?family=Roboto+Condensed:wght@700&family=Open+Sans:wght@600;700&family=Arimo:wght@700&display=swap">
<style>
  :root {
    --burgundy: #7a3432;
    --headline-gold: #d9a23a;
    --white: #ffffff;
    --band: #1f2224;
    --figure-tint: rgba(255, 255, 255, 0.22);
  }
  * { margin: 0; padding: 0; box-sizing: border-box; }
  html, body {
    width: 1200px; height: 805px; overflow: hidden;
    background: var(--band);
  }
  .sign {
    position: relative;
    width: 1200px; height: 805px;
    overflow: hidden;
  }
  .sunburst {
    position: absolute; left: 0; top: 0;
    width: 1200px; height: 611px;
    display: block;
  }
  .figure {
    position: absolute;
    background: radial-gradient(ellipse at center, var(--figure-tint), rgba(255,255,255,0.08) 75%);
    border-radius: 40px;
  }
  .headline {
    position: absolute; left: 0; width: 1200px;
    text-align: center;
  }
  .headline-offer {
    top: 98px;
    font-family: "Roboto Condensed", "Arial Narrow", sans-serif;
    font-weight: 700;
    font-size: 72px;
    line-height: 1;
    color: var(--headline-gold);
    margin-left: 6px;
  }
  .headline-classes {
    top: 190px;
    font-family: "Roboto Condensed", "Arial Narrow", sans-serif;
    font-weight: 700;
    font-size: 46px;
    line-height: 1;
    color: var(--headline-gold);
  }
  .headline-schedule {
    top: 240px;
    font-family: "Open Sans", Arial, sans-serif;
    font-weight: 700;
    font-size: 78px;
    line-height: 1;
    color: var(--white);
    letter-spacing: 1px;
  }
  .footer-band {
    position: absolute; left: 0; top: 611px;
    width: 1200px; height: 194px;
    background: var(--band);
  }
  .studio-name {
    position: absolute; left: 40px; top: 54px;
    display: flex; align-items: center; gap: 18px;
  }
  .studio-dot {
    width: 58px; height: 58px; border-radius: 50%;
    background: var(--headline-gold);
  }
  .studio-wordmark {
    font-family: "Open Sans", Arial, sans-serif;
    font-weight: 600;
    font-size: 44px;
    color: var(--white);
    white-space: nowrap;
  }
  .studio-address {
    position: absolute; left: 619px; right: 12px; top: 52px;
    font-family: "Arimo", Arial, sans-serif;
    font-weight: 700;
    font-size: 36px;
    line-height: 50px;
    color: var(--white);
    font-style: normal;
    white-space: nowrap;
  }
</style>
</head>
<body>
<main class="sign">
  <svg class="sunburst" viewBox="0 0 1200 611" preserveAspectRatio="none" aria-hidden="true">
    <defs>
      <linearGradient id="ray-gold" x1="0" y1="0" x2="0" y2="1">
        <stop offset="0" stop-color="#8a3a2e"/>
        <stop offset="1" stop-color="#f4b010"/>
      </linearGradient>
      <linearGradient id="ray-ember" x1="0" y1="0" x2="0" y2="1">
        <stop offset="0" stop-color="#7e3430"/>
        <stop offset="1" stop-color="#d8431c"/>
      </linearGradient>
      <linearGradient id="ray-flame" x1="0" y1="0" x2="0" y2="1">
        <stop offset="0" stop-color="#80362f"/>
        <stop offset="1" stop-color="#e0702a"/>
      </linearGradient>
      <linearGradient id="ray-red" x1="0" y1="0" x2="1" y2="0">
        <stop offset="0" stop-color="#8a3530"/>
        <stop offset="1" stop-color="#e04634"/>
      </linearGradient>
    </defs>
    <rect width="1200" height="611" fill="var(--burgundy)"/>
    <polygon points="0,0 180,0 0,330" fill="url(#ray-gold)" opacity="0.8"/>
    <polygon points="600,-300 -200,611 -200,340" fill="url(#ray-ember)"/>
    <polygon points="600,-300 120,611 -120,611" fill="url(#ray-gold)"/>
    <polygon points="600,-300 430,611 330,611" fill="url(#ray-ember)"/>
    <polygon points="600,-300 680,611 570,611" fill="url(#ray-gold)" opacity="0.55"/>
    <polygon points="600,-300 840,611 750,611" fill="url(#ray-flame)" opacity="0.7"/>
    <polygon points="600,-300 1040,611 910,611" fill="url(#ray-flame)"/>
    <polygon points="600,-300 1400,611 1400,420" fill="url(#ray-flame)"/>
    <polygon points="600,-300 1400,250 1400,0 1050,-300" fill="url(#ray-red)"/>
  </svg>

  <div class="figure" role="img" aria-label="White silhouette of a woman in a standing side-bend pose" style="left:167px;top:43px;width:113px;height:151px"></div>
  <div class="figure" role="img" aria-label="White silhouette of a seated woman stretching one leg back" style="left:65px;top:221px;width:172px;height:124px"></div>
  <div class="figure" role="img" aria-label="White silhouette of a woman in a bridge with one leg raised" style="left:199px;top:388px;width:210px;height:118px"></div>
  <div class="figure" role="img" aria-label="White silhouette of a woman in a reverse plank" style="left:485px;top:442px;width:210px;height:97px"></div>
  <div class="figure" role="img" aria-label="White silhouette of a woman in a shoulder stand" style="left:722px;top:393px;width:108px;height:167px"></div>
  <div class="figure" role="img" aria-label="White silhouette of a woman kneeling with one leg lifted" style="left:916px;top:329px;width:167px;height:167px"></div>
  <div class="figure" role="img" aria-label="White silhouette of a woman doing a plank on an exercise ball" style="left:975px;top:92px;width:205px;height:129px"></div>

  <h1 class="headline headline-offer">Pilates &amp; Kinovane</h1>
  <p class="headline headline-classes">classes</p>
  <p class="headline headline-schedule">7 Days a Week</p>

  <footer class="footer-band">
    <div class="studio-name">
      <span class="studio-dot" aria-hidden="true"></span>
      <span class="studio-wordmark">Lark Hollow Pilates</span>
    </div>
    <address class="studio-address">
      2140 Alder Lane #12 Aptos.<br>
      CA 95003 831.555.0142
    </address>
  </footer>
</main>
</body>
</html>
```